M Zyvantics Buisness Cards

I need a technology focused clean business card for my employees. I have attached out logo to include in the mocks. We're a modern tech consulting firm that drives to interface humanity with technology in a truly cohesive fashion.

```html
<!DOCTYPE html>
<html lang="en">
<head>
<meta charset="utf-8">
<title>M Zyvantics Business Cards</title>
<link rel="stylesheet" href="https://fonts.googleapis.com/css2?family=Lato:wght@400;700&family=Oswald:wght@600&display=swap">
<style>
  :root {
    --stage: #3b3b3b;
    --stage-edge: #2c2c2c;
    --brand-blue: #1c74bd;
    --card-white: #ffffff;
    --ink: #1b1b1b;
    --rule: #1c74bd;
  }
  * { box-sizing: border-box; margin: 0; padding: 0; }
  html, body { width: 1200px; height: 900px; overflow: hidden; }
  body {
    background: radial-gradient(ellipse at center, var(--stage) 0%, var(--stage-edge) 100%);
    font-family: "Lato", sans-serif;
    position: relative;
  }
  .card {
    position: absolute;
    width: 580px;
    height: 330px;
    box-shadow: 0 18px 40px rgba(0,0,0,0.45);
  }
  /* Back of card */
  .card-back {
    left: 540px;
    top: 90px;
    background: var(--brand-blue);
    color: var(--card-white);
  }
  .brand-lockup {
    position: absolute;
    left: 0; right: 0;
    top: 120px;
    display: flex;
    align-items: center;
    justify-content: center;
    gap: 18px;
  }
  .brand-dot {
    width: 30px; height: 30px;
    border-radius: 50%;
    background: var(--card-white);
  }
  .brand-name {
    font-family: "Lato", sans-serif;
    font-weight: 700;
    font-size: 52px;
    letter-spacing: 4px;
    color: var(--card-white);
  }
  .back-web {
    position: absolute;
    left: 0; right: 0;
    bottom: 38px;
    text-align: center;
    font-size: 15px;
    letter-spacing: 1px;
  }
  /* Front of card */
  .card-front {
    left: 80px;
    top: 470px;
    background: var(--card-white);
    color: var(--ink);
  }
  .card-front::after {
    content: "";
    position: absolute;
    left: 0; right: 0; bottom: 0;
    height: 8px;
    background: var(--brand-blue);
  }
  .identity {
    position: absolute;
    right: 330px;
    top: 88px;
    text-align: right;
  }
  .person-name {
    font-family: "Oswald", sans-serif;
    font-weight: 600;
    font-size: 34px;
    line-height: 1.1;
    color: var(--brand-blue);
    letter-spacing: -0.5px;
    white-space: nowrap;
  }
  .person-role {
    font-size: 17px;
    margin-top: 2px;
  }
  .divider {
    position: absolute;
    left: 282px;
    top: 82px;
    width: 2px;
    height: 92px;
    background: var(--rule);
  }
  .contact-list {
    position: absolute;
    left: 316px;
    top: 86px;
    list-style: none;
  }
  .contact-list li {
    display: flex;
    align-items: center;
    gap: 12px;
    font-size: 17px;
    line-height: 22px;
  }
  .contact-list svg { width: 14px; height: 14px; fill: var(--brand-blue); flex: none; }
  .address {
    position: absolute;
    left: 0; right: 0;
    bottom: 36px;
    text-align: center;
    font-size: 19px;
  }
</style>
</head>
<body>
  <section class="card card-back" aria-label="Card back">
    <div class="brand-lockup">
      <span class="brand-dot"></span>
      <span class="brand-name">M ZYVANTICS</span>
    </div>
    <p class="back-web">www.zyvantics.com</p>
  </section>

  <section class="card card-front" aria-label="Card front">
    <div class="identity">
      <h1 class="person-name">DANA HOLLOWAY</h1>
      <p class="person-role">Manager</p>
    </div>
    <div class="divider"></div>
    <ul class="contact-list">
      <li>
        <svg viewBox="0 0 24 24" aria-hidden="true"><path d="M6.6 10.8a15.1 15.1 0 0 0 6.6 6.6l2.2-2.2a1 1 0 0 1 1-.25 11.4 11.4 0 0 0 3.6.57 1 1 0 0 1 1 1V20a1 1 0 0 1-1 1A17 17 0 0 1 3 4a1 1 0 0 1 1-1h3.5a1 1 0 0 1 1 1c0 1.25.2 2.45.57 3.57a1 1 0 0 1-.25 1z"/></svg>
        512 555 0140
      </li>
      <li>
        <svg viewBox="0 0 24 24" aria-hidden="true"><path d="M7 1h10a2 2 0 0 1 2 2v18a2 2 0 0 1-2 2H7a2 2 0 0 1-2-2V3a2 2 0 0 1 2-2zm0 3v13h10V4zm5 15a1.2 1.2 0 1 0 0 2.4A1.2 1.2 0 0 0 12 19z"/></svg>
        512 555 0141
      </li>
      <li>
        <svg viewBox="0 0 24 24" aria-hidden="true"><path d="M2 5h20v14H2zm2 2v.5l8 5 8-5V7zm0 2.8V17h16V9.8l-8 5z"/></svg>
        info@zyvantics.com
      </li>
      <li>
        <svg viewBox="0 0 24 24" aria-hidden="true"><path d="M12 2a10 10 0 1 0 0 20 10 10 0 0 0 0-20zm6.9 6h-2.9a15.7 15.7 0 0 0-1.4-3.6A8 8 0 0 1 18.9 8zM12 4c.8 1.2 1.5 2.5 1.9 4h-3.8c.4-1.5 1.1-2.8 1.9-4zM4.3 14a8.2 8.2 0 0 1 0-4h3.4a16.5 16.5 0 0 0 0 4zm.8 2h2.9c.3 1.3.8 2.5 1.4 3.6A8 8 0 0 1 5.1 16zM8 8H5.1a8 8 0 0 1 4.3-3.6C8.8 5.5 8.3 6.7 8 8zm4 12c-.8-1.2-1.5-2.5-1.9-4h3.8c-.4 1.5-1.1 2.8-1.9 4zm2.3-6H9.7a14.7 14.7 0 0 1 0-4h4.6a14.7 14.7 0 0 1 0 4zm.3 5.6c.6-1.1 1.1-2.3 1.4-3.6h2.9a8 8 0 0 1-4.3 3.6zm1.7-5.6a16.5 16.5 0 0 0 0-4h3.4a8.2 8.2 0 0 1 0 4z"/></svg>
        www.zyvantics.com
      </li>
    </ul>
    <p class="address">48 Alder Court, Houston, TX 77002</p>
  </section>
</body>
</html>
```